Brightwell Recovery Email Marketing Design

Dear Designer,
We're in need of an email background template for our company, Brightwell Recovery, that reflects our commitment to building lasting relationships with our clients and providing top-quality restoration and cleaning services.
We'd like the template to incorporate our brand colors, which are #F2F2F3, #005EA5, #468ECC, and #000000, and to feature images related to our services, such as water restoration, emergency flood response, mold remediation, trauma scene clean-up, fire restoration, carpet cleaning, and more. Our logo and tagline, "Calm Returns", should be prominently displayed in a unique and visually appealing way, along with our website address, www.brightwellrecovery.example.
The email should be professional and positive, highlighting the camaraderie and teamwork among our employees. We want to thank our clients for their business, offer a special discount, and promote our services. The final design should be visually stunning and memorable, with a clear call-to-action to encourage clients to take advantage of the discount.
We'd like the final design in JPG or PNG format, with a resolution of at least 720x720 pixels.
Thank you for considering this project. We're excited to see what you come up with!
Best regards,
Tavin

```html
<!DOCTYPE html>
<html lang="en">
<head>
<meta charset="utf-8">
<title>Brightwell Recovery – Calm Returns</title>
<link rel="stylesheet" href="https://fonts.googleapis.com/css2?family=Sorts+Mill+Goudy&family=PT+Sans:wght@400;700&display=swap">
<style>
  :root {
    --brand-navy: #1f4e84;
    --brand-sky: #1ca6ea;
    --ink-dark: #101215;
    --paper: #ffffff;
    --paper-soft: #f2f2f3;
    --icon-water: #b9bdbd;
    --icon-mold: #c9ccd3;
    --icon-fire: #5b5048;
    --icon-trauma: #6b4a1e;
  }
  * { margin: 0; padding: 0; box-sizing: border-box; }
  html, body { width: 1200px; height: 1200px; overflow: hidden; background: var(--ink-dark); }
  .email-card { position: relative; width: 1200px; height: 1200px; overflow: hidden; font-family: "PT Sans", sans-serif; color: var(--paper); }

  .header-rain {
    position: absolute; left: 0; top: 0; width: 1200px; height: 153px;
    background: radial-gradient(ellipse at 50% 40%, #3a3d42 0%, #18191c 70%, #0c0c0e 100%);
  }
  .brand-name {
    position: absolute; left: 0; top: 0; width: 1200px; height: 153px;
    display: flex; align-items: center; justify-content: center;
    font-family: "Sorts Mill Goudy", serif; font-size: 46px; letter-spacing: 2px;
    color: var(--paper-soft); text-transform: uppercase;
  }

  .title-band {
    position: absolute; left: 0; top: 153px; width: 1200px; height: 155px;
    background: var(--brand-navy);
    display: flex; align-items: center; justify-content: center;
  }
  .title-band h1 {
    font-family: "Sorts Mill Goudy", serif; font-weight: 400; font-size: 76px;
    letter-spacing: 2px; text-transform: uppercase; color: var(--paper);
  }

  .room-backdrop {
    position: absolute; left: 0; top: 308px; width: 1200px; height: 795px;
    background: linear-gradient(180deg, #1a1c1f 0%, #24272b 40%, #1c1e21 75%, #121315 100%);
  }

  .service { position: absolute; display: flex; align-items: center; }
  .service-icon {
    width: 140px; height: 140px; border-radius: 50%;
    border: 5px solid var(--brand-navy); flex: none;
  }
  .icon-water { background: radial-gradient(circle at 40% 40%, #d6d8d7, var(--icon-water) 60%, #7d7f80); }
  .icon-mold { background: radial-gradient(circle at 50% 45%, #eef0f4, var(--icon-mold) 55%, #3b5378); }
  .icon-fire { background: radial-gradient(circle at 50% 50%, #8a7766, var(--icon-fire) 60%, #2d2824); }
  .icon-trauma { background: radial-gradient(circle at 50% 50%, #c78a2a, var(--icon-trauma) 55%, #2a1d10); }
  .service-name {
    margin-left: 32px; font-family: "Sorts Mill Goudy", serif; font-size: 32px;
    line-height: 50px; text-transform: uppercase; color: var(--paper);
  }
  .service-water { left: 100px; top: 342px; }
  .service-mold { left: 683px; top: 342px; }
  .service-fire { left: 100px; top: 540px; }
  .service-trauma { left: 683px; top: 540px; }

  .intro-copy {
    position: absolute; left: 110px; top: 712px; width: 980px;
    font-size: 26px; line-height: 49px; text-align: center; color: var(--paper);
  }
  .offer-line {
    position: absolute; left: 110px; top: 916px; width: 980px;
    font-size: 26px; line-height: 49px; text-align: center;
    font-weight: 700; color: var(--brand-sky);
  }

  .thanks-row { position: absolute; left: 103px; top: 1000px; display: flex; gap: 15px; }
  .thanks-label {
    width: 347px; height: 58px; background: var(--brand-sky);
    display: flex; align-items: center; justify-content: center;
    font-weight: 700; font-size: 26px; text-transform: uppercase; color: var(--paper);
    margin-right: 22px;
  }
  .client-tile {
    width: 134px; height: 58px; background: var(--paper); border-radius: 4px;
    display: flex; align-items: center; justify-content: center; gap: 6px;
    font-size: 17px; color: var(--brand-navy);
  }
  .client-dot { width: 10px; height: 10px; border-radius: 50%; background: var(--brand-navy); }

  .footer-band {
    position: absolute; left: 0; top: 1103px; width: 1200px; height: 97px;
    background: var(--brand-navy);
    display: flex; align-items: center; justify-content: center;
    font-size: 30px; color: var(--paper);
  }
</style>
</head>
<body>
  <main class="email-card">
    <div class="header-rain" role="img" aria-label="Dark background of water droplets on glass"></div>
    <div class="brand-name">Brightwell Recovery</div>

    <section class="title-band"><h1>Calm Returns</h1></section>

    <div class="room-backdrop" role="img" aria-label="Dim photo of an empty interior room with large windows"></div>

    <div class="service service-water">
      <div class="service-icon icon-water" role="img" aria-label="Photo of water damage on a wall"></div>
      <p class="service-name">Water<br>Restoration</p>
    </div>
    <div class="service service-mold">
      <div class="service-icon icon-mold" role="img" aria-label="Photo of a technician in a protective suit"></div>
      <p class="service-name">Mold<br>Remediation</p>
    </div>
    <div class="service service-fire">
      <div class="service-icon icon-fire" role="img" aria-label="Photo of a fire-damaged interior"></div>
      <p class="service-name">Fire and Smoke<br>Restoration</p>
    </div>
    <div class="service service-trauma">
      <div class="service-icon icon-trauma" role="img" aria-label="Photo of a cordoned-off scene at night"></div>
      <p class="service-name">Trauma<br>Clean Up</p>
    </div>

    <p class="intro-copy">Our friendly team of experienced professionals are ready to get started on your cleaning project. Brightwell Recovery knows how to deliver the results you deserve – every time. Give us a call and we can be to you within an hour anywhere in Las Vegas.</p>
    <p class="offer-line">Thank-you offer: 15% off your next service – call today to claim it!</p>

    <div class="thanks-row">
      <div class="thanks-label">We thank our clients :</div>
      <div class="client-tile"><span class="client-dot"></span>Rivermark</div>
      <div class="client-tile"><span class="client-dot"></span>Tidepoint</div>
      <div class="client-tile"><span class="client-dot"></span>Lumen Lab</div>
      <div class="client-tile">Northfield</div>
    </div>

    <footer class="footer-band">www.brightwellrecovery.example.</footer>
  </main>
</body>
</html>
```